Crime Novel Book Cover

I need a book cover for a crime novel - a psychological thriller aimed primarily at women. The book is called KELP (in capital letters.) The design sound show a brick wall with the word 'KELP' written across it in dripping red blood. I picture the word slanted down the wall (if this would work.) Then there would be flames rising up and around the wall. At the bottom would be my name - Tamsin Verholt. I want to use this cover for both the ebook and the print version so it would need to work for both. The cover would need to look good thumbnail size as this is how it will be viewed online. I would like the writing in big bold letters so that it stands out if this would look good.

Online

```html
<!DOCTYPE html>
<html lang="en">
<head>
<meta charset="utf-8">
<title>KELP – Tamsin Verholt</title>
<link rel="stylesheet" href="https://fonts.googleapis.com/css2?family=Creepster&family=Questrial&display=swap">
<style>
  :root {
    --bg-core: #4c0400;
    --bg-mid: #2a0100;
    --bg-edge: #120000;
    --fire-light: #ff8a1c;
    --fire-mid: #e0520a;
    --fire-deep: #8a1a04;
    --fire-char: #3a0a02;
    --author: #ffffff;
  }
  html, body {
    margin: 0;
    padding: 0;
    overflow: hidden;
    background: var(--bg-edge);
  }
  .cover {
    position: relative;
    width: 1054px;
    height: 1200px;
    overflow: hidden;
    background: radial-gradient(ellipse 70% 60% at 42% 45%, var(--bg-core) 0%, var(--bg-mid) 45%, var(--bg-edge) 100%);
  }
  .cover__title {
    position: absolute;
    left: 0;
    right: 0;
    top: 150px;
    margin: 0;
    text-align: center;
    font-family: "Creepster", cursive;
    font-weight: 400;
    font-size: 380px;
    line-height: 1;
    letter-spacing: -6px;
    transform: scale(1.02, 1.45);
    transform-origin: top center;
    background: linear-gradient(115deg,
      var(--fire-char) 0%,
      var(--fire-deep) 18%,
      var(--fire-mid) 32%,
      var(--fire-char) 44%,
      var(--fire-deep) 55%,
      var(--fire-mid) 68%,
      var(--fire-light) 82%,
      var(--fire-mid) 100%);
    -webkit-background-clip: text;
    background-clip: text;
    color: transparent;
  }
  .cover__author {
    position: absolute;
    left: 0;
    right: 0;
    top: 1030px;
    margin: 0;
    text-align: center;
    font-family: "Questrial", sans-serif;
    font-size: 86px;
    line-height: 1;
    letter-spacing: 1px;
    color: var(--author);
  }
</style>
</head>
<body>
  <main class="cover">
    <h1 class="cover__title">KELP</h1>
    <p class="cover__author">Tamsin Verholt</p>
  </main>
</body>
</html>
```